Video Thumbnail Design for Jazz Piano YouTube channel

Hello, my name’s Marcus Fenwick. I run a jazz piano YouTube channel called ‘Keyhaven Lessons’ (www.vidstreamer.example/keyhavenlessons). It’s the most subscribed to jazz piano YouTube channel with over 200,000 subscribers.

I need a designer to create an eye-catching thumbnail, to be used for my upcoming videos.

BRIEF:
For now, I’m asking for just one thumbnail design. I will choose a designer from this initial project, and I plan to commission additional designs from the same designer - so that my thumbnails all have a coherent look.

WHAT MAKES A GOOD THUMBNAIL:
Above all, your thumbnail design must be EYE-CATCHING and STAND OUT. Imagine scrolling through hundreds of YouTube videos - the video’s thumbnail artwork is one of the key aspects that gets someone to click and watch a video, so this is a VERY important aspect to getting views.

Your design can be innovative - surprise me. I want your design to JUMP OUT at me. For example, you could experiment with creating a 3D effect, or having elements popping out of the frame. A YouTube thumbnail doesn’t have to be square to the edges - you can add white around the edges to create an unusual jagged effect (when viewed in YouTube's search, which has a white background), and certain things could come out of the picture (see attached files for reference).

Remember, YouTube thumbnails are displayed very small - especially on desktop. It’s a good idea to design your thumbnail at this small size, rather than at full size on your computer screen. You'll probably need to zoom in closer to my face and enlarge the text more than you normally would if you were creating a larger image.

Lots of contrast is needed in a tiny thumbnail. Blacks must be pitch black, whites must be white, color saturation - the thumbnail must contain a lot of energy in a small space.

A strong format for YouTube thumbnails is to have a FACE (my face) and TEXT (large white text, 3 - 5 words). You can use this if you like, or you can experiment with a different format. I’m completely open to your ideas.

BRAND LOOK & FEEL:
Here are some keywords that describe my brand:
- Calm
- Professional
- Sophisticated (jazz is a sophisticated style of music)
View my channel to see my visual style as a starting point: www.vidstreamer.example/keyhavenlessons

BRAND COLORS:
- Turquoise: Hex #00DBD7 (this is my main brand color and must be used in the thumbnail)
- Black
- White
- Red: #FC5B5B (I sometimes use this as a secondary color - you can use this in your design if you want, or not).

TEXT:
The font I use for my brand is ‘Lovelo’ (please use this font in your design - included in my attachment).
I like my text to be white against a black background.
For your design, you could use the text: 'SWEET CHORD VOICING' as sample text.

IMAGES:
I've attached several photos for you to work with - just choose one for your design. The backgrounds are not important to the Thumbnail - only me and the piano are needed - so it's up to you whether you black out the background, darken it, or leave it in. Feel free to zoom in, rotate at an angle, distort, etc.

SLANTS:
I like diagonal lines and slants - because they go well with the ‘jazz’ feel. This could include the text itself (at an angle instead of straight), or the picture (any images of me or the piano could be at an angle, rather than straight).

DIMENSIONS:
YouTube thumbnails must be 1280 pixels wide by 720 pixels tall. A ratio of 16:9 is ideal as it’s used most often in YouTube players and previews.

DELIVERABLES:
If your design is selected - I will need a Photoshop file delivered of the final design (this is so that I can edit the text myself to make it relevant to the video).

After that, I will commission further designs with you (these will be separate projects, each with its own payment). My end goal is to have 10 - 15 strong thumbnail designs - all from the same designer.

Thank you very much for your submission, I can't wait to see what you come up with!

Target Market(s)

My audience is 90% male, between 25 - 65 years old. I have viewers worldwide, but they mostly live in the US and Canada.

Font styles to use
Other font styles liked:
• Lovelo

Colors
31b7a3

Requirements
Must have
• Image and text (as described in the project description)
Nice to have
• Creative use of white edges to stand out on YouTube (against other traditional square looking thumbnails).
• See full description in the project description.

```html
<!DOCTYPE html>
<html lang="en">
<head>
<meta charset="utf-8">
<title>Sweet Chord Voicing – thumbnail</title>
<link rel="stylesheet" href="https://fonts.googleapis.com/css2?family=Montserrat:wght@800&display=swap">
<style>
  :root {
    --turquoise: #00dbd7;
    --red: #fc5b5b;
    --amber: #e8a829;
    --white: #ffffff;
    --key-ivory: #e6c9a0;
    --key-shadow: #c9a97c;
    --sepia-light: #d8c6ae;
    --sepia-mid: #b9a58c;
    --sepia-dark: #2a2420;
  }
  html, body {
    margin: 0;
    padding: 0;
    width: 1200px;
    height: 675px;
    overflow: hidden;
    background: var(--white);
  }
  .thumbnail {
    display: block;
    width: 1200px;
    height: 675px;
  }
  .bg { fill: var(--turquoise); }
  .accent-stripe { fill: var(--amber); }
  .title-band { fill: var(--red); }
  .speed-lines line { stroke: var(--white); stroke-width: 2; }
  .keyboard-band { fill: url(#keyboardTone); }
  .host-photo { fill: url(#sepiaTone); }
  .title-text {
    font-family: "Montserrat", sans-serif;
    font-weight: 800;
    font-size: 56px;
    fill: var(--white);
  }
</style>
</head>
<body>
<svg class="thumbnail" viewBox="0 0 1280 720" xmlns="http://www.w3.org/2000/svg">
  <defs>
    <linearGradient id="keyboardTone" x1="0" y1="0" x2="1" y2="1">
      <stop offset="0" stop-color="var(--key-ivory)"/>
      <stop offset="1" stop-color="var(--key-shadow)"/>
    </linearGradient>
    <linearGradient id="sepiaTone" x1="0" y1="0" x2="0" y2="1">
      <stop offset="0" stop-color="var(--sepia-light)"/>
      <stop offset="0.65" stop-color="var(--sepia-mid)"/>
      <stop offset="1" stop-color="var(--sepia-dark)"/>
    </linearGradient>
  </defs>

  <rect class="bg" x="0" y="0" width="1280" height="720"/>

  <g class="speed-lines">
    <line x1="370" y1="0" x2="1330" y2="720"/>
    <line x1="395" y1="0" x2="1355" y2="720"/>
    <line x1="420" y1="0" x2="1380" y2="720"/>
    <line x1="445" y1="0" x2="1405" y2="720"/>
    <line x1="470" y1="0" x2="1430" y2="720"/>
    <line x1="495" y1="0" x2="1455" y2="720"/>
    <line x1="520" y1="0" x2="1480" y2="720"/>
    <line x1="545" y1="0" x2="1505" y2="720"/>
    <line x1="570" y1="0" x2="1530" y2="720"/>
    <line x1="595" y1="0" x2="1555" y2="720"/>
    <line x1="620" y1="0" x2="1580" y2="720"/>
    <line x1="645" y1="0" x2="1605" y2="720"/>
    <line x1="670" y1="0" x2="1630" y2="720"/>
  </g>

  <polygon class="keyboard-band" role="img" aria-label="Diagonal piano keyboard with ivory and black keys"
           points="0,0 110,0 1070,720 560,720 0,300"/>

  <polygon class="accent-stripe" points="0,330 0,356 488,722 522,722"/>

  <polygon class="accent-stripe" points="292,0 322,0 1282,720 1252,720"/>

  <polygon class="title-band" points="150,0 292,0 1252,720 1110,720"/>

  <text class="title-text" x="0" y="0" text-anchor="middle" dominant-baseline="central"
        textLength="690" lengthAdjust="spacingAndGlyphs"
        transform="translate(702 362) rotate(38)">SWEET CHORD VOICING</text>

  <path class="host-photo" role="img" aria-label="Sepia head-and-shoulders portrait of the channel host in a dark jacket"
        d="M40,720 L40,660 C60,600 110,585 150,560 C140,520 130,470 125,430
           C110,420 108,370 122,360 C118,290 125,210 185,175 C250,140 340,150 385,190
           C420,225 425,300 410,360 C425,370 420,420 405,440 C400,490 390,530 375,560
           C440,580 520,610 560,680 L575,720 Z"/>
</svg>
</body>
</html>
```